For Lease sign for Property management company in Kansas City

We need someone to take our information and design a standard for lease sign that we can put in front of each of our buildings. I would love for it to do its job of letting people know there are units available but also be unique somehow. Also the aspect ratio of the design would ideally be 4 wide by 3 tall but we open to other ideas. It will be a larger yard sign.

Target Market(s)

Potential Tenants

Industry/Entity Type

Real Estate Development

Font styles to use
Sans Serif

Requirements
Must have
• Our logo, our website (www.quillstead-properties.com), our phone number (816) 555-2719.
Nice to have
• Some how say "For Lease"
Sign to be 4' wide by 3' tall
If there was a place to put the building name that would be cool but not ne
Should not have
• Nothing that I can think of

```html
<!DOCTYPE html>
<html lang="en">
<head>
<meta charset="utf-8">
<title>Quillstead Properties – For Lease Sign</title>
<link rel="stylesheet" href="https://fonts.googleapis.com/css2?family=Montserrat:wght@600;700&family=Oswald:wght@700&display=swap">
<style>
  :root {
    --backdrop: #231f20;
    --brand-red: #be1e2d;
    --brand-red-dark: #8e1520;
    --brand-yellow: #fbb040;
    --brand-yellow-edge: #e89a2e;
    --panel-light: #f4f4f4;
    --panel-grey: #cfd0d2;
    --white: #ffffff;
  }
  html, body {
    margin: 0;
    padding: 0;
    width: 1200px;
    height: 1200px;
    overflow: hidden;
    background: var(--backdrop);
  }
  .canvas {
    position: relative;
    width: 1200px;
    height: 1200px;
  }
  .lease-sign {
    position: absolute;
    left: 100px;
    top: 225px;
    width: 1000px;
    height: 750px;
    display: block;
  }
  .headline {
    font-family: "Oswald", "Arial Narrow", sans-serif;
    font-weight: 700;
    fill: var(--brand-red);
  }
  .brand-name {
    font-family: "Montserrat", Arial, sans-serif;
    font-weight: 700;
    fill: var(--brand-red);
  }
  .website {
    font-family: "Montserrat", Arial, sans-serif;
    font-weight: 600;
    font-size: 33px;
    fill: var(--white);
  }
  .website .website-name { fill: var(--brand-yellow); }
  .phone-number {
    font-family: "Montserrat", Arial, sans-serif;
    font-weight: 700;
    font-size: 94px;
    fill: var(--white);
  }
</style>
</head>
<body>
<main class="canvas">
  <svg class="lease-sign" viewBox="0 0 1000 750" xmlns="http://www.w3.org/2000/svg" role="img" aria-label="Quillstead Properties for lease sign">
    <defs>
      <linearGradient id="panel-light-gradient" x1="0" y1="0" x2="1" y2="0">
        <stop offset="0" stop-color="var(--panel-grey)"/>
        <stop offset="0.55" stop-color="var(--panel-light)"/>
        <stop offset="1" stop-color="var(--white)"/>
      </linearGradient>
    </defs>

    <!-- left brand panel -->
    <rect class="brand-panel" x="0" y="0" width="1000" height="605" fill="url(#panel-light-gradient)"/>

    <!-- angled headline panel -->
    <polygon class="headline-stripe" points="556,0 1000,0 1000,598 391,598" fill="var(--brand-red)"/>
    <polygon class="headline-panel" points="570,0 1000,0 1000,598 405,598" fill="var(--brand-yellow)"/>

    <text class="headline headline-for" x="775" y="210" font-size="118" text-anchor="middle" textLength="182" lengthAdjust="spacingAndGlyphs">FOR</text>
    <text class="headline headline-lease" x="764" y="357" font-size="170" text-anchor="middle" textLength="412" lengthAdjust="spacingAndGlyphs">LEASE</text>

    <!-- website ribbon -->
    <polygon class="website-fold" points="397,448 445,430 445,448" fill="var(--brand-red-dark)"/>
    <polygon class="website-ribbon" points="397,448 1000,448 1000,516 387,516" fill="var(--brand-red)"/>
    <text class="website" x="416" y="494" textLength="566" lengthAdjust="spacingAndGlyphs">www.<tspan class="website-name">quillstead-properties</tspan>.com</text>

    <!-- brand mark -->
    <circle class="brand-dot" cx="209" cy="233" r="145" fill="var(--brand-yellow)" stroke="var(--brand-yellow-edge)" stroke-width="3"/>
    <text class="brand-name" x="52" y="450" font-size="44" textLength="322" lengthAdjust="spacingAndGlyphs">QUILLSTEAD</text>
    <text class="brand-name" x="52" y="502" font-size="44" textLength="322" lengthAdjust="spacingAndGlyphs">PROPERTIES</text>

    <!-- contact band -->
    <rect class="divider" x="0" y="598" width="1000" height="8" fill="var(--white)"/>
    <rect class="contact-band" x="0" y="605" width="1000" height="145" fill="var(--brand-red)"/>

    <g class="phone-icon" fill="none" stroke="var(--brand-yellow)" stroke-linecap="round">
      <path d="M50,650 c-12,8 -14,22 -6,36 c10,18 26,32 44,40 c12,5 22,2 28,-8 l-16,-14 c-4,3 -8,6 -12,4 c-10,-5 -18,-13 -23,-23 c-2,-4 0,-8 4,-11 z" fill="var(--brand-yellow)" stroke="none"/>
      <path d="M80,660 a18,18 0 0 1 18,18" stroke-width="5"/>
      <path d="M82,644 a34,34 0 0 1 32,32" stroke-width="5"/>
      <path d="M84,628 a50,50 0 0 1 46,46" stroke-width="5"/>
    </g>
    <text class="phone-number" x="150" y="712" textLength="780" lengthAdjust="spacingAndGlyphs">(816) 555-2719</text>
  </svg>
</main>
</body>
</html>
```